Business card design needed

We would like a new design for our window furnishings & home decor business. We supply & install blinds, curtains, shutters etc. We are about to incorporate home decor products like cushoins & throws...
We'd like to use moderns browns & green tones. Casual but elegant style. Maybe textured/patterned look design. Design should communicate quality and great value with latest designs.

website & FB page & email is still to be advised so pls provide space.

Industry/Entity Type

Business

Contact Information for Business Card

Marlowe Haven
Window Furnishings & Home Decor
Genevieve - Interior Stylist
Call us now for a free measure & quote - 63124089
0412 906 358
0418 273 564

```html
<!DOCTYPE html>
<html lang="en">
<head>
<meta charset="utf-8">
<title>Marlowe Haven – Business Cards</title>
<link rel="stylesheet" href="https://fonts.googleapis.com/css2?family=Cinzel:wght@400;500&display=swap">
<style>
  :root {
    --stage: #1f1f21;
    --brown-deep: #3f2f17;
    --brown: #5a4622;
    --olive: #5f6a2c;
    --green: #5f9a48;
    --green-glow: #7dbb5e;
    --frame: rgba(225, 225, 205, 0.75);
    --ink: #ffffff;
    --card-w: 560px;
    --card-h: 320px;
  }
  * { box-sizing: border-box; margin: 0; padding: 0; }
  html, body {
    width: 1200px; height: 900px; overflow: hidden;
    background: var(--stage);
  }
  .stage {
    position: relative; width: 1200px; height: 900px;
    display: flex; flex-direction: column; align-items: center; justify-content: center; gap: 60px;
  }
  .card {
    position: relative; width: var(--card-w); height: var(--card-h);
    overflow: hidden; color: var(--ink);
    font-family: "Cinzel", "Times New Roman", serif;
    box-shadow: 0 10px 30px rgba(0,0,0,0.55);
  }
  .card__texture { position: absolute; inset: 0; }
  .card--back .card__texture {
    background:
      radial-gradient(ellipse 50% 55% at 45% 45%, var(--green-glow) 0%, rgba(95,154,72,0.6) 35%, rgba(95,154,72,0) 75%),
      linear-gradient(135deg, var(--brown) 0%, var(--olive) 30%, var(--green) 50%, var(--brown) 82%, var(--brown-deep) 100%);
  }
  .card--front .card__texture {
    background:
      radial-gradient(ellipse 45% 60% at 72% 38%, var(--green-glow) 0%, rgba(95,154,72,0.65) 35%, rgba(95,154,72,0) 80%),
      linear-gradient(110deg, var(--brown-deep) 0%, var(--brown) 35%, var(--olive) 60%, var(--green) 100%);
  }
  .card__frame {
    position: absolute; inset: 14px;
    border: 1.5px solid var(--frame);
    outline: 1px solid rgba(225,225,205,0.35); outline-offset: -5px;
  }
  .card__content {
    position: absolute; inset: 0;
    display: flex; flex-direction: column; justify-content: center; align-items: center; text-align: center;
    text-shadow: 0 1px 2px rgba(0,0,0,0.35);
    white-space: nowrap;
  }
  .cta__headline { font-size: 26px; letter-spacing: 0.5px; line-height: 1.1; }
  .cta__offer {
    font-size: 19px; letter-spacing: 0.5px; margin-top: 2px; padding-bottom: 3px;
    border-bottom: 1.5px solid var(--ink);
  }
  .contact__phones { font-size: 18px; margin-top: 30px; letter-spacing: 0.4px; }
  .contact__online { font-size: 11.5px; margin-top: 10px; letter-spacing: 0.6px; }
  .card--front .card__content {
    align-items: flex-end; padding: 0 44px 10px 44px;
  }
  .brand { text-align: left; }
  .brand__name {
    font-size: 29px; font-weight: 500; letter-spacing: 0.3px; line-height: 1.1;
    white-space: nowrap;
  }
  .brand__tagline {
    font-size: 16px; letter-spacing: 0.3px; margin-left: 40px; margin-top: 2px;
    white-space: nowrap;
  }
</style>
</head>
<body>
  <main class="stage">
    <section class="card card--back">
      <div class="card__texture" role="img" aria-label="Subtle green and brown damask pattern background"></div>
      <div class="card__frame"></div>
      <div class="card__content">
        <p class="cta__headline">CALL US NOW</p>
        <p class="cta__offer">FOR A FREE MEASURE &amp; QUOTE</p>
        <p class="contact__phones">63124089 - 0412 906 358 - 0418 273 564</p>
        <p class="contact__online">INFO@MARLOWEHAVEN.NET - SOCIAL.PAGE/MARLOWEHAVEN</p>
      </div>
    </section>

    <section class="card card--front">
      <div class="card__texture" role="img" aria-label="Subtle brown to green damask pattern background"></div>
      <div class="card__frame"></div>
      <div class="card__content">
        <div class="brand">
          <h1 class="brand__name">MARLOWE HAVEN WINDOW</h1>
          <p class="brand__tagline">Furnishings &amp; Home Decor Genevieve</p>
        </div>
      </div>
    </section>
  </main>
</body>
</html>
```